I am a company selling interior designing materials

HI, I am selling interior design materials and require a namecard which is more outstanding while following a certain details placement as attached.

My clients are mainly interior designers so it has to attract their attention rather than feeling that its "just another namecard". I am selling wallcoverings, fabrics, acoustics and carpets.

Target Market(s)

interior designers designing hotels, commerical offices.

Contact Information for Business Card

As per attached.
Please change address to 47 Jalan 16 Tampines #05-02 Velmora Building Singapore 527314

Font styles to use
Other font styles liked:
• calibri

Requirements
Must have
• (1) company logo on top in the middle. Placement of contac details to be the same
• (2) company color is blue/green cymk 75/8/42/0
• (3) "KTV" logo to be prominent
• (4) You may change the logo but there should be a "swirl" surrounding the word KTV like current logo. The swirl pattern does not need to follow current logo and you may propose.
Should not have
• (1) there should not be any designs above "KTV" logo
• (2) no sharp triangles or angles

```html
<!DOCTYPE html>
<html lang="en">
<head>
<meta charset="utf-8">
<title>KTV Business Card</title>
<link rel="stylesheet" href="https://fonts.googleapis.com/css2?family=Carlito:wght@400;700&display=swap">
<style>
  :root {
    --brand-teal: #23afa3;
    --brand-teal-dark: #1a978c;
    --ink-grey: #555a5c;
    --ink-dark: #3c4042;
    --accent-red: #e0262b;
    --rule-grey: #9a9d9f;
    --card-white: #f7f7f7;
    --page-bg: #dcdedf;
  }
  * { box-sizing: border-box; margin: 0; padding: 0; }
  html, body {
    width: 1200px; height: 886px; overflow: hidden;
    background: var(--page-bg);
    font-family: "Carlito", "Calibri", sans-serif;
    color: var(--ink-grey);
  }
  .sheet {
    position: relative; width: 1200px; height: 886px;
    display: flex; flex-direction: column; align-items: center; justify-content: center; gap: 44px;
  }
  .card {
    position: relative; width: 620px; height: 372px;
    background: var(--card-white); border-radius: 24px; overflow: hidden;
    box-shadow: 0 6px 18px rgba(0,0,0,.18);
  }

  /* Back of card */
  .card-back .brand-mark {
    position: absolute; right: 58px; top: 70px;
    display: flex; align-items: center; gap: 14px;
  }
  .brand-dot { width: 22px; height: 22px; border-radius: 50%; background: var(--brand-teal); }
  .brand-name-large {
    font-size: 92px; font-weight: 700; color: var(--ink-grey); letter-spacing: 2px; line-height: 1;
  }
  .card-back .company-block { position: absolute; left: 44px; bottom: 40px; }
  .company-name { font-size: 17px; font-weight: 700; color: var(--ink-grey); }
  .product-list { margin-top: 4px; font-size: 16px; color: var(--ink-grey); }
  .product-list .sep { color: var(--accent-red); margin: 0 6px; }

  /* Front of card */
  .card-front .identity {
    position: absolute; left: 40px; top: 96px; width: 330px; text-align: center;
  }
  .identity .brand-row { display: flex; justify-content: center; align-items: center; gap: 10px; }
  .identity .brand-dot { width: 14px; height: 14px; }
  .brand-name-small { font-size: 50px; font-weight: 700; color: var(--ink-grey); letter-spacing: 1px; line-height: 1; }
  .identity .company-name { font-size: 14px; margin-top: 8px; }
  .divider {
    position: absolute; left: 388px; top: 80px; width: 1px; height: 150px; background: var(--rule-grey);
  }
  .contact { position: absolute; left: 408px; top: 84px; width: 200px; }
  .person-name { font-size: 24px; font-weight: 700; color: var(--brand-teal); letter-spacing: .5px; text-transform: uppercase; }
  .address { margin-top: 10px; font-size: 15px; line-height: 1.25; color: var(--ink-dark); }
  .contact-line { display: flex; align-items: center; gap: 8px; font-size: 15px; color: var(--ink-dark); margin-top: 4px; }
  .contact-line svg { flex: none; }
  .base-band { position: absolute; left: 0; bottom: 0; }
  .website {
    position: absolute; right: 34px; bottom: 22px;
    color: #fff; font-size: 18px; letter-spacing: 4px;
  }
</style>
</head>
<body>
<main class="sheet">

  <section class="card card-back" aria-label="Card back">
    <div class="brand-mark">
      <span class="brand-dot"></span>
      <span class="brand-name-large">KTV</span>
    </div>
    <div class="company-block">
      <p class="company-name">KaiTeVale Interior Furnishings Pte Ltd</p>
      <p class="product-list">Wallcoverings<span class="sep">•</span>Acoustic<span class="sep">•</span>Fabrics<span class="sep">•</span>Carpet</p>
    </div>
  </section>

  <section class="card card-front" aria-label="Card front">
    <div class="identity">
      <div class="brand-row">
        <span class="brand-dot"></span>
        <span class="brand-name-small">KTV</span>
      </div>
      <p class="company-name">KaiTeVale Interior Furnishings Pte Ltd</p>
    </div>

    <div class="divider"></div>

    <div class="contact">
      <p class="person-name">Lena Hartono</p>
      <p class="address">47 Jalan 16 Tampines #05-02<br>Velmora Building Singapore 527314</p>
      <p class="contact-line">
        <svg width="12" height="16" viewBox="0 0 12 16" aria-hidden="true"><rect x="1" y="1" width="10" height="14" rx="2" fill="none" stroke="var(--brand-teal)" stroke-width="1.6"/><circle cx="6" cy="12.5" r="1" fill="var(--brand-teal)"/></svg>
        (65) 9172 4460
      </p>
      <p class="contact-line">
        <svg width="14" height="10" viewBox="0 0 14 10" aria-hidden="true"><rect x="0" y="0" width="14" height="10" rx="1.5" fill="var(--brand-teal)"/><path d="M1 1.5 L7 6 L13 1.5" fill="none" stroke="#fff" stroke-width="1.2"/></svg>
        lena@ktvfurnishing.com
      </p>
    </div>

    <svg class="base-band" width="620" height="90" viewBox="0 0 620 90" aria-hidden="true">
      <defs>
        <linearGradient id="bandFill" x1="0" y1="0" x2="1" y2="0">
          <stop offset="0" stop-color="var(--brand-teal)"/>
          <stop offset="1" stop-color="var(--brand-teal-dark)"/>
        </linearGradient>
      </defs>
      <path d="M0 40 H232 C246 40 246 22 262 22 H620" fill="none" stroke="var(--rule-grey)" stroke-width="3"/>
      <path d="M0 48 H236 C250 48 250 30 266 30 H620 V90 H0 Z" fill="url(#bandFill)"/>
    </svg>
    <p class="website">www.ktvfurnishing.com</p>
  </section>

</main>
</body>
</html>
```